Bref créative
Real Estate Development Firm
Marlow Holdings
I need double sided standard sized Business Card [3.5" x 2"]
May use same font as in logo or other suggestions
Professional
Derek P. Hollins
President/CEO
248 West Penrose Street
Suite 2360
Milwaukee, WI 53217
dhollins@marlowholdingsllc.example
marlowholdingsllc.example
You can refer to logo design contest for other ideas.
Logo and design or color gradient or other suggestions.
Please use logo

```html
<!DOCTYPE html>
<html lang="en">
<head>
<meta charset="utf-8">
<title>Marlow Holdings – Business Card</title>
<link href="https://fonts.googleapis.com/css2?family=Cinzel:wght@400;500&family=EB+Garamond:wght@400;500;600&display=swap" rel="stylesheet">
<style>
  :root {
    --panel-light: #d9d9d9;
    --panel-mid: #9a9a9a;
    --panel-dark: #6c6c6c;
    --band-grey: #7b7b7b;
    --paper: #ffffff;
    --brand-blue: #33428a;
    --mark-blue: #4c5d9e;
    --ink: #111111;
    --on-grey: #ffffff;
  }
  html, body {
    margin: 0;
    padding: 0;
    width: 1200px;
    height: 1049px;
    overflow: hidden;
    background: #ffffff;
  }
  .card {
    position: relative;
    width: 1200px;
    height: 1049px;
    font-family: "EB Garamond", Georgia, serif;
  }
  .front {
    position: absolute;
    left: 0; top: 0;
    width: 597px; height: 1049px;
    background: radial-gradient(ellipse 330px 380px at 299px 360px, var(--panel-light) 0%, var(--panel-mid) 45%, var(--panel-dark) 100%);
  }
  .front .brand-dot {
    position: absolute;
    left: 239px; top: 250px;
    width: 120px; height: 120px;
    border-radius: 50%;
    background: var(--mark-blue);
  }
  .front .brand-name {
    position: absolute;
    left: 0; width: 597px;
    top: 615px;
    text-align: center;
    font-family: "Cinzel", Georgia, serif;
    font-weight: 400;
    font-size: 44px;
    color: var(--on-grey);
    margin: 0;
    letter-spacing: 1px;
  }
  .identity {
    position: absolute;
    left: 597px; top: 0;
    width: 603px; height: 762px;
    background: var(--paper);
    text-align: center;
  }
  .identity .brand-dot {
    position: absolute;
    left: 261px; top: 80px;
    width: 82px; height: 82px;
    border-radius: 50%;
    background: var(--mark-blue);
  }
  .identity .brand-name {
    position: absolute;
    left: 0; width: 603px; top: 254px;
    margin: 0;
    font-family: "Cinzel", Georgia, serif;
    font-weight: 400;
    font-size: 42px;
    color: var(--brand-blue);
  }
  .identity .rule {
    position: absolute;
    left: 67px; width: 469px; top: 312px;
    height: 2px;
    background: var(--brand-blue);
  }
  .identity .tagline {
    position: absolute;
    left: 0; width: 603px; top: 316px;
    margin: 0;
    font-family: "Cinzel", Georgia, serif;
    font-size: 27px;
    color: var(--ink);
    letter-spacing: 1px;
  }
  .identity .person {
    position: absolute;
    left: 0; width: 603px; top: 452px;
    margin: 0;
    font-size: 56px;
    font-weight: 500;
    color: var(--ink);
  }
  .identity .role {
    position: absolute;
    left: 0; width: 603px; top: 530px;
    margin: 0;
    font-size: 31px;
    font-weight: 600;
    color: var(--ink);
  }
  .identity .online {
    position: absolute;
    left: 0; width: 603px; top: 658px;
    font-size: 31px;
    font-weight: 600;
    color: var(--ink);
    line-height: 42px;
  }
  .contact {
    position: absolute;
    left: 597px; top: 762px;
    width: 603px; height: 287px;
    background: var(--band-grey);
    color: var(--on-grey);
  }
  .contact .address {
    position: absolute;
    left: 46px; width: 557px; top: 28px;
    margin: 0;
    text-align: center;
    font-style: normal;
    font-size: 30px;
    line-height: 40px;
  }
  .contact .lines {
    position: absolute;
    left: 58px; top: 160px;
    margin: 0;
    font-size: 27px;
    line-height: 34px;
    border-collapse: collapse;
  }
  .contact .lines td { padding: 0; }
  .contact .lines .label { width: 117px; }
</style>
</head>
<body>
  <div class="card">
    <section class="front">
      <div class="brand-dot"></div>
      <p class="brand-name">Marlow Holdings</p>
    </section>

    <section class="identity">
      <div class="brand-dot"></div>
      <p class="brand-name">Marlow Holdings</p>
      <div class="rule"></div>
      <p class="tagline">Vision Built to Last</p>
      <h1 class="person">Derek P. Hollins</h1>
      <p class="role">President / CEO</p>
      <div class="online">
        <div>dhollins@marlowholdingsllc.example</div>
        <div>www.marlowholdingsllc.example</div>
      </div>
    </section>

    <section class="contact">
      <address class="address">248 West Penrose Street<br>Suite 2360 Milwaukee, WI 53217</address>
      <table class="lines">
        <tr><td class="label">Phone</td><td>: 414.555.0140</td></tr>
        <tr><td class="label">Cell</td><td>: 414.555.0187</td></tr>
        <tr><td class="label">Fax</td><td>: 414.555.0141</td></tr>
      </table>
    </section>
  </div>
</body>
</html>
```